Oil Field Service company needs professional business cards

Looking to clean up our current company business cards and look a little more professional. Harlow Tubular Services is a US based company that services the oil field. We deal with engineers, managers and oil rigs....................................................................................................................................................................................................................................................................................................................................................................................................

Target Market(s)

Oil and Gas professionals

Industry/Entity Type

Oil And Gas

Contact Information for Business Card

See attached photo as example

Font styles to use
Sans Serif

Colors
ec1f27

Requirements
Must have
• Company Logo, Name, Title, Cell, Office, Fax, Email.
• See attached photo
Nice to have
• External CRT, Internal CRT, Casing Crews, Torque Turn, Laydown Machine
Should not have
• Do not introduce any new pictures and keep it professional looking

```html
<!DOCTYPE html>
<html lang="en">
<head>
<meta charset="utf-8">
<title>Harlow Tubular Services – Business Card</title>
<link href="https://fonts.googleapis.com/css2?family=Open+Sans:wght@400;600;700;800&display=swap" rel="stylesheet">
<style>
  :root {
    --bg: #e9e7e3;
    --paper: #ffffff;
    --slate: #4c5d6b;
    --slate-soft: #6f7d88;
    --red: #ec1f27;
    --ink: #3a4550;
    --muted: #6a747c;
    --rule: #c9cdd1;
  }
  * { box-sizing: border-box; margin: 0; padding: 0; }
  html, body { width: 1200px; height: 1062px; overflow: hidden; }
  body {
    background: var(--bg);
    font-family: "Open Sans", Arial, sans-serif;
    color: var(--ink);
    display: flex;
    flex-direction: column;
    align-items: center;
    justify-content: center;
    gap: 70px;
  }
  .card {
    position: relative;
    width: 595px;
    height: 340px;
    background: var(--paper);
    box-shadow: 0 10px 30px rgba(0,0,0,0.12);
    overflow: hidden;
  }
  .card-front {
    display: flex;
    align-items: center;
    justify-content: center;
  }
  .wordmark {
    color: var(--slate-soft);
    font-weight: 800;
    text-transform: uppercase;
    text-align: center;
    line-height: 1.05;
    white-space: nowrap;
  }
  .card-front .wordmark { font-size: 46px; letter-spacing: 1px; }
  .wordmark .sub { display: block; font-size: 0.42em; letter-spacing: 5px; margin-top: 8px; }
  .card-back .wordmark { font-size: 36px; }

  .band {
    position: absolute;
    left: 0;
    right: 0;
    height: 22px;
    background: var(--slate);
  }
  .band-top { top: 0; border-bottom: 3px solid var(--red); }
  .band-bottom { bottom: 0; border-top: 3px solid var(--red); }

  .back-content {
    position: absolute;
    top: 25px;
    bottom: 25px;
    left: 0;
    right: 0;
    display: flex;
    align-items: center;
    padding: 0 48px;
    gap: 30px;
  }
  .person { width: 215px; flex: none; }
  .person-name { font-weight: 700; font-size: 19px; color: var(--ink); }
  .person-title { font-size: 14px; color: var(--muted); margin-top: 2px; }
  .contact-list {
    list-style: none;
    margin-top: 20px;
    padding-top: 14px;
    border-top: 1px solid var(--rule);
    font-size: 14px;
    color: var(--muted);
  }
  .contact-list li { display: flex; align-items: center; gap: 9px; line-height: 1.75; white-space: nowrap; }
  .contact-list svg { width: 12px; height: 12px; flex: none; fill: var(--muted); }
  .brand { flex: 1; display: flex; justify-content: center; }
</style>
</head>
<body>
  <section class="card card-front">
    <div class="wordmark">Harlow<span class="sub">Tubular Services</span></div>
  </section>

  <section class="card card-back">
    <div class="band band-top"></div>
    <div class="band band-bottom"></div>
    <div class="back-content">
      <div class="person">
        <div class="person-name">Cole Brannigan</div>
        <div class="person-title">Area Manager</div>
        <ul class="contact-list">
          <li><svg viewBox="0 0 12 12" aria-hidden="true"><path d="M2.5 1 4.5 3.5 3.5 4.8Q4.8 7.4 7.2 8.5L8.5 7.5 11 9.5 9.6 11Q4.6 10.6 1 2.4Z"/></svg>123-456-7890</li>
          <li><svg viewBox="0 0 12 12" aria-hidden="true"><path d="M3 1H9V11H3ZM4 2V9H8V2Z"/></svg>123-456-7890</li>
          <li><svg viewBox="0 0 12 12" aria-hidden="true"><circle cx="6" cy="6" r="5" fill="none" stroke="#6a747c" stroke-width="1.2"/><path d="M1 6H11M6 1V11" stroke="#6a747c" stroke-width="1"/></svg>www.harlowtubular.com</li>
          <li><svg viewBox="0 0 12 12" aria-hidden="true"><circle cx="6" cy="6" r="2" fill="none" stroke="#6a747c" stroke-width="1.2"/><path d="M8 4V7.5Q8 9 9.5 8.5Q11 7.5 11 6A5 5 0 1 0 8.5 10.3" fill="none" stroke="#6a747c" stroke-width="1.2"/></svg>info@harlowtubular.com</li>
        </ul>
      </div>
      <div class="brand">
        <div class="wordmark">Harlow<span class="sub">Tubular Services</span></div>
      </div>
    </div>
  </section>
</body>
</html>
```